Stock Market Research Company Needs a new Design for our Podcast

We need a new logo and social media images for our podcast called Ledger Chat Show. We have a current design and logo but are looking to update the branding of the podcast. The podcast is highly interactive taking listener questions each week on individual stocks as well as stock portfolio building strategies.

Copy of Ledger Chat Show Thumbnail is our current branding.

Podcast Ad 2 Image attached for an idea of what we're looking for but using our specific colours.

Incorporate K from our current logo (attached)
Colours: Primary Color: (#1AA897), Secondary Color (#2E4151)
Clean/Modern style
Include Headshots of Hosts (images attached)

Target Market(s)

Podcast listeners and stock market investors

Industry/Entity Type

Investment

Logo Text

Title - Ledger Chat Show. Tagline - Stock Picks, Strategies & Tips For All Investors

Colors
33b8a4
86cfc6
00a990

Requirements
Must have
• Incorporate K from our current logo (attached)
Clean/Modern style

```html
<!DOCTYPE html>
<html lang="en">
<head>
<meta charset="utf-8">
<title>Ledger Chat Show – Thumbnail</title>
<link href="https://fonts.googleapis.com/css2?family=Oswald:wght@700&family=Roboto+Slab:wght@500;700&family=Raleway:wght@500&display=swap" rel="stylesheet">
<style>
  :root {
    --teal: #20a898;
    --navy: #2e4151;
    --page: #5e5e5e;
    --bg-light: #eef2f4;
    --bg-mid: #d9e1e6;
    --white: #ffffff;
  }
  * { box-sizing: border-box; }
  html, body {
    margin: 0;
    width: 1200px;
    height: 1200px;
    overflow: hidden;
    background: var(--page);
  }
  h1, p { margin: 0; }
  .thumbnail {
    position: absolute;
    left: 0;
    top: 240px;
    width: 1200px;
    height: 720px;
    overflow: hidden;
    background: var(--bg-light);
  }
  .backdrop {
    position: absolute;
    inset: 0;
    background: linear-gradient(160deg, #f3f6f8 0%, var(--bg-mid) 45%, #e6ecef 70%, #f1f4f6 100%);
  }
  .title-main {
    position: absolute;
    left: 72px;
    top: 65px;
    width: 611px;
    height: 167px;
    background: var(--teal);
    color: var(--white);
    font-family: 'Oswald', sans-serif;
    font-weight: 700;
    font-size: 104px;
    line-height: 140px;
    text-align: center;
    letter-spacing: 1px;
    white-space: nowrap;
  }
  .title-sub {
    position: absolute;
    left: 194px;
    top: 205px;
    width: 447px;
    height: 93px;
    background: var(--navy);
    color: var(--white);
    font-family: 'Roboto Slab', serif;
    font-weight: 700;
    font-size: 66px;
    line-height: 93px;
    text-align: center;
    letter-spacing: 6px;
  }
  .brand-mark {
    position: absolute;
    left: 906px;
    top: 65px;
    width: 59px;
    height: 59px;
    background: var(--teal);
  }
  .brand {
    position: absolute;
    left: 730px;
    top: 133px;
    width: 410px;
    text-align: center;
    color: var(--navy);
    font-family: 'Raleway', sans-serif;
    font-weight: 500;
  }
  .brand-name {
    font-size: 35px;
    line-height: 44px;
    letter-spacing: 1px;
    white-space: nowrap;
  }
  .brand-tagline {
    font-size: 15px;
    line-height: 20px;
    letter-spacing: 3.4px;
    margin-top: 10px;
    white-space: nowrap;
  }
  .tagline {
    position: absolute;
    left: 72px;
    top: 432px;
    color: var(--navy);
    font-family: 'Roboto Slab', serif;
    font-weight: 500;
    font-size: 46px;
    line-height: 72px;
    white-space: nowrap;
  }
  .host {
    position: absolute;
    bottom: 0;
    height: 383px;
    border-radius: 160px 160px 0 0;
  }
  .host-one {
    left: 530px;
    width: 380px;
    background: linear-gradient(180deg, #c9a896 0%, #d8bba9 35%, #3a4452 60%, #2a323d 100%);
  }
  .host-two {
    left: 880px;
    width: 320px;
    background: linear-gradient(180deg, #e2b8a4 0%, #e9c3b0 35%, #50565e 60%, #3d434a 100%);
  }
</style>
</head>
<body>
  <main class="thumbnail">
    <div class="backdrop" role="img" aria-label="Blurred photo of financial bar and line charts with a hand pointing at a rising graph"></div>

    <h1 class="title-main">LEDGER CHAT</h1>
    <div class="title-sub">SHOW</div>

    <div class="brand-mark"></div>
    <div class="brand">
      <p class="brand-name">NORTHGATE CAPITAL</p>
      <p class="brand-tagline">INDEPENDENT EQUITY ADVISORS</p>
    </div>

    <p class="tagline">STOCK PICKS,<br>STRATEGIES &amp; TIP<br>FOR INVESTORS</p>

    <div class="host host-one" role="img" aria-label="Headshot of the first host in a dark suit and white shirt"></div>
    <div class="host host-two" role="img" aria-label="Headshot of the second host wearing glasses, grey suit and white shirt"></div>
  </main>
</body>
</html>
```